Business card

creative business card for newly created national firm that specializes in high-density storage for retail markets. Looking for creativity and overall theme that will differentiate from others in this unique niche ...essentially a design that will provide instant recognition as we develop our identity in the marketplace. possible initial thoughts are attached with logo separately

Retail

```html
<!DOCTYPE html>
<html lang="en">
<head>
<meta charset="utf-8">
<title>Stackwise Storage – Business Card</title>
<link rel="stylesheet" href="https://fonts.googleapis.com/css2?family=Marcellus+SC&family=Questrial&display=swap">
<style>
  :root {
    --page: #ffffff;
    --ink-deep: #1b4e68;
    --ink-body: #3a4650;
    --sky: #4bbdf0;
    --blue-mid: #2a86cf;
    --blue-deep: #1f4a8c;
    --silver-light: #fbfbfb;
    --silver-mid: #d9dadc;
    --white: #ffffff;
  }
  * { margin: 0; padding: 0; box-sizing: border-box; }
  html, body {
    width: 998px; height: 1200px; overflow: hidden;
    background: var(--page);
  }
  .card {
    position: absolute;
    width: 817px; height: 484px;
    overflow: hidden;
    box-shadow: 0 6px 14px rgba(0,0,0,0.25);
    background: linear-gradient(90deg, var(--silver-mid) 0%, var(--silver-light) 45%, var(--silver-light) 70%, var(--silver-mid) 100%);
  }
  .card--front { left: 86px; top: 78px; }
  .card--back  { left: 88px; top: 632px; }
  .card__bands { position: absolute; inset: 0; width: 100%; height: 100%; }

  .brand {
    position: absolute; left: 72px; top: 100px;
    display: flex; align-items: center; gap: 16px;
  }
  .brand__name {
    font-family: "Questrial", sans-serif;
    font-size: 46px; line-height: 1.15;
    color: var(--ink-deep);
    letter-spacing: 1px;
    white-space: nowrap;
  }
  .brand__mark { width: 56px; height: 56px; background: var(--sky); flex: none; }

  .contact-head {
    position: absolute; left: 448px; top: 132px;
    font-family: "Marcellus SC", serif; color: var(--ink-deep);
    white-space: nowrap;
  }
  .contact-head__name { font-size: 30px; letter-spacing: 1px; }
  .contact-head__phone { font-size: 23px; margin-top: 6px; letter-spacing: 0.5px; }

  .tagline, .web {
    position: absolute; left: 0; width: 100%; text-align: center;
    font-family: "Marcellus SC", serif; color: var(--white);
    white-space: nowrap;
  }
  .tagline { top: 334px; font-size: 42px; letter-spacing: 3px; }
  .card--front .web { top: 410px; font-size: 23px; letter-spacing: 1.5px; }
  .card--back .web { top: 398px; font-size: 27px; letter-spacing: 1.5px; }

  .layer-fade {
    position: absolute; left: 534px; top: 0; width: 283px; height: 345px;
    background: linear-gradient(100deg, rgba(160,215,240,0) 0%, rgba(150,210,238,0.55) 55%, rgba(190,228,245,0.35) 100%);
  }

  .details {
    position: absolute; left: 96px; top: 80px; list-style: none;
    font-family: "Questrial", sans-serif; font-size: 22px; color: var(--ink-body);
  }
  .details li { display: flex; align-items: center; height: 44px; white-space: nowrap; }
  .details svg { width: 22px; height: 22px; margin-right: 16px; fill: none; stroke: var(--ink-deep); stroke-width: 1.8; flex: none; }
</style>
</head>
<body>

<section class="card card--front">
  <svg class="card__bands" viewBox="0 0 817 484" preserveAspectRatio="none" aria-hidden="true">
    <defs>
      <linearGradient id="front-silver" x1="0" x2="1">
        <stop offset="0" stop-color="#eeeeef"/><stop offset="0.55" stop-color="#8e9195"/><stop offset="1" stop-color="#c9cacc"/>
      </linearGradient>
      <linearGradient id="front-blue" x1="0" y1="0" x2="0" y2="1">
        <stop offset="0" stop-color="#4bbdf0"/><stop offset="0.45" stop-color="#2a86cf"/><stop offset="1" stop-color="#1f4a8c"/>
      </linearGradient>
    </defs>
    <path d="M0 312 Q408 250 817 318 L817 484 L0 484 Z" fill="url(#front-silver)"/>
    <path d="M0 322 Q408 264 817 330 L817 484 L0 484 Z" fill="url(#front-blue)"/>
  </svg>

  <div class="brand">
    <div class="brand__name">STACKWISE<br>STORAGE</div>
    <div class="brand__mark"></div>
  </div>

  <div class="contact-head">
    <div class="contact-head__name">Dana Whitfield</div>
    <div class="contact-head__phone">844-STACK-NOW</div>
  </div>

  <div class="tagline">INNOVATE YOUR SPACE</div>
  <div class="web">WWW.STACKWISESTORAGE.COM</div>
</section>

<section class="card card--back">
  <div class="layer-fade" role="img" aria-label="Soft layered blue panel decoration"></div>

  <svg class="card__bands" viewBox="0 0 817 484" preserveAspectRatio="none" aria-hidden="true">
    <defs>
      <linearGradient id="back-silver" x1="0" x2="1">
        <stop offset="0" stop-color="#eeeeef"/><stop offset="0.55" stop-color="#8e9195"/><stop offset="1" stop-color="#c9cacc"/>
      </linearGradient>
      <linearGradient id="back-blue" x1="0" y1="0" x2="0" y2="1">
        <stop offset="0" stop-color="#4bbdf0"/><stop offset="0.45" stop-color="#2a86cf"/><stop offset="1" stop-color="#1f4a8c"/>
      </linearGradient>
    </defs>
    <path d="M0 330 Q408 292 817 336 L817 484 L0 484 Z" fill="url(#back-silver)"/>
    <path d="M0 342 Q408 304 817 348 L817 484 L0 484 Z" fill="url(#back-blue)"/>
  </svg>

  <ul class="details">
    <li><svg viewBox="0 0 24 24"><path d="M2 10 L12 3 L22 10 M4 9 V21 H20 V9 M9 21 V14 H15 V21"/></svg>418 W. Juniper Ave. Millbrook, AZ 86011</li>
    <li><svg viewBox="0 0 24 24"><rect x="2" y="5" width="20" height="14"/><path d="M2 5 L12 13 L22 5"/></svg>PO Box 2710, Millbrook, AZ 86012</li>
    <li><svg viewBox="0 0 24 24"><path d="M6 2 L10 6 L8 9 Q10 14 15 16 L18 14 L22 18 L19 22 Q6 20 2 5 Z"/></svg>(844) Stack-Now</li>
    <li><svg viewBox="0 0 24 24"><rect x="6" y="2" width="12" height="20" rx="2"/><path d="M10 18 H14"/></svg>(330) 555-0147</li>
    <li><svg viewBox="0 0 24 24"><path d="M2 9 L12 3 L22 9 V21 H2 Z M2 9 L12 15 L22 9"/></svg>dana@stackwisestorage.com</li>
  </ul>

  <div class="web">WWW.STACKWISESTORAGE.COM</div>
</section>

</body>
</html>
```